card design for engineering consultancy

engineering drafting and project management company the provides drafting services for.
Electrical, Hydraulic, Mechanical, and Civil services
The company is called Q7R Services and logo is as attached
Information on card should be.
1. Logo
2.website : Q7RServices.example
3. email : info@Q7RServices.example
4. Phone: (+61) 400512836
5. Motto: Design - Document - Develop - Deliver

this card should be basically used for business identification only

Target Market(s)

electricians plumbers air conditioning installers and civil contractors

Industry/Entity Type

engineering, drafting, electrical, plumbing, airconditioning, civil

Contact Information for Business Card

1. Logo 2.website : Q7RServices.example 3. email : info@Q7RServices.example 4. Phone: (+61) 400512836 5. Motto: Design - Document - Develop - Deliver

Font styles to use
Serif

Requirements
Must have
• logo
Nice to have
• something inovative and different that makes it stand out from being just another business card

```html
<!DOCTYPE html>
<html lang="en">
<head>
<meta charset="utf-8">
<title>Q7R Services – Business Card</title>
<link rel="stylesheet" href="https://fonts.googleapis.com/css2?family=Michroma&family=Audiowide&display=swap">
<style>
  :root {
    --backdrop: #cccccc;
    --card-black: #0b0c0e;
    --card-charcoal: #1f2528;
    --brand-red: #ff0a14;
    --deep-red: #b80006;
    --dark-red: #6e0003;
    --logo-grey: #3b4446;
    --steel: #c9cdcf;
    --ink: #0a0a0a;
  }
  * { margin: 0; padding: 0; box-sizing: border-box; }
  html, body {
    width: 1200px; height: 846px; overflow: hidden;
    background: var(--backdrop);
  }
  .card {
    position: absolute; left: 346px; width: 508px; height: 291px;
    overflow: hidden;
    background: linear-gradient(135deg, var(--card-charcoal) 0%, var(--card-black) 45%, #050607 100%);
  }
  .card--front { top: 113px; }
  .card--back  { top: 443px; }

  .decor-panel {
    position: absolute; left: 0; top: 0; width: 250px; height: 156px;
    background: linear-gradient(180deg, #050505 0%, #121416 55%, var(--dark-red) 100%);
  }
  .decor-accent {
    position: absolute; left: 0; top: 262px; width: 92px; height: 12px;
    background: linear-gradient(90deg, var(--deep-red), var(--dark-red));
  }

  .brand-name {
    position: absolute; left: 270px; top: 130px; width: 227px;
    display: flex; align-items: center; justify-content: center;
    font-family: "Michroma", sans-serif; font-size: 14px; line-height: 1;
    letter-spacing: 2.6px; color: var(--logo-grey);
    text-transform: uppercase; white-space: nowrap;
  }
  .brand-mark {
    display: inline-block; width: 11px; height: 11px; margin-right: 8px;
    background: var(--logo-grey); flex: none;
  }

  .contact-band {
    position: absolute; left: 0; top: 171px; width: 508px; height: 76px;
    background: linear-gradient(90deg, var(--deep-red) 0%, #ea0007 50%, var(--brand-red) 100%);
  }
  .contact-list { position: absolute; left: 101px; top: 7px; list-style: none; }
  .contact-list li {
    display: flex; align-items: center; height: 22px;
    font-family: "Audiowide", sans-serif; font-size: 13px; color: var(--ink);
    text-transform: uppercase; letter-spacing: 0.2px;
  }
  .contact-icon { width: 16px; height: 16px; margin-right: 5px; flex: none; }

  .motto {
    position: absolute; left: 102px; top: 259px; width: 386px;
    font-family: "Audiowide", sans-serif; font-style: italic; font-size: 14px;
    color: var(--brand-red); text-transform: uppercase; letter-spacing: 1.1px;
    white-space: nowrap;
  }

  .back-name {
    position: absolute; left: 0; right: 0; top: 181px;
    text-align: center; font-family: "Michroma", sans-serif; font-size: 19px;
    letter-spacing: 4px; color: var(--steel); text-transform: uppercase;
    white-space: nowrap;
  }
</style>
</head>
<body>
  <section class="card card--front" aria-label="Card front">
    <div class="decor-panel" role="img" aria-label="Angular dark and red technical line decoration"></div>
    <div class="decor-accent" role="img" aria-label="Small red accent shape"></div>

    <h1 class="brand-name"><span class="brand-mark"></span>Q7R Services</h1>

    <div class="contact-band">
      <ul class="contact-list">
        <li>
          <svg class="contact-icon" viewBox="0 0 16 16" aria-hidden="true">
            <rect width="16" height="16" rx="4" fill="#0a0a0a"/>
            <circle cx="8" cy="8" r="5" fill="none" stroke="#e00" stroke-width="1"/>
            <ellipse cx="8" cy="8" rx="2.2" ry="5" fill="none" stroke="#e00" stroke-width="0.9"/>
            <line x1="3" y1="8" x2="13" y2="8" stroke="#e00" stroke-width="0.9"/>
          </svg>www.Q7RServices.example
        </li>
        <li>
          <svg class="contact-icon" viewBox="0 0 16 16" aria-hidden="true">
            <rect width="16" height="16" rx="4" fill="#0a0a0a"/>
            <rect x="3.5" y="5" width="9" height="6.5" fill="none" stroke="#e00" stroke-width="0.9"/>
            <polyline points="3.5,5 8,9 12.5,5" fill="none" stroke="#e00" stroke-width="0.9"/>
          </svg>info@Q7RServices.example
        </li>
        <li>
          <svg class="contact-icon" viewBox="0 0 16 16" aria-hidden="true">
            <rect width="16" height="16" rx="4" fill="#0a0a0a"/>
            <path d="M4.5 3.5 L6.5 3.5 L7.3 6 L6 7 Q7 9.3 9 10 L10 8.7 L12.5 9.5 L12.5 11.5 Q12 12.6 10.5 12.5 Q4 11.5 3.5 5.5 Q3.4 4 4.5 3.5 Z" fill="#e00"/>
          </svg>(+61) 400512836
        </li>
      </ul>
    </div>

    <p class="motto">Design - Document - Develop - Deliver</p>
  </section>

  <section class="card card--back" aria-label="Card back">
    <p class="back-name">Q7R Services</p>
  </section>
</body>
</html>
```